Need a graphic design to promote our new online learning system

We are seeking a graphic design to be promoted on social media to promote our new Online earning Management system (ZOR-LMS). The purpose is to make the design attractive and informative for parents and students so they can enrol at our School.

It must state the benefits of the ZOR-LMS. Colourful but not too busy.

```html
<!DOCTYPE html>
<html lang="en">
<head>
<meta charset="utf-8">
<title>Zorvale Academy – Enroll Online</title>
<link rel="stylesheet" href="https://fonts.googleapis.com/css2?family=Bitter:wght@400;600;700&family=Roboto+Slab:wght@600;700&display=swap">
<style>
  :root{
    --navy:#00468f;
    --sand:#ece09a;
    --band:#e8dfbf;
    --white:#ffffff;
    --button-top:#f6ecb4;
    --button-bottom:#e6d585;
    --spark:#f3e7a6;
  }
  html,body{margin:0;padding:0;overflow:hidden;background:var(--sand);}
  .canvas{position:relative;width:1200px;height:1200px;overflow:hidden;}
  .backdrop{position:absolute;inset:0;width:1200px;height:1200px;display:block;}
  .brand{
    position:absolute;left:0;width:586px;top:150px;
    display:flex;align-items:center;justify-content:center;gap:14px;
    font-family:"Bitter",serif;font-weight:600;font-size:42px;color:var(--navy);
    letter-spacing:1px;line-height:1;
  }
  .brand-square{width:26px;height:26px;background:var(--navy);}
  .headline{
    position:absolute;margin:0;font-family:"Roboto Slab",serif;color:var(--white);
    line-height:1;white-space:nowrap;
  }
  .headline-top{left:112px;top:400px;font-size:86px;font-weight:700;}
  .headline-mid{left:202px;top:500px;font-size:86px;font-weight:700;}
  .headline-big{left:84px;top:566px;font-size:292px;font-weight:600;letter-spacing:-6px;}
  .enroll-button{
    position:absolute;left:80px;top:948px;width:559px;height:78px;box-sizing:border-box;
    border-radius:12px;background:linear-gradient(var(--button-top),var(--button-bottom));
    font-family:"Bitter",serif;font-size:41px;color:var(--navy);white-space:nowrap;
    display:flex;align-items:center;padding-left:30px;text-decoration:none;
  }
  .cursor-icon{position:absolute;left:610px;top:975px;width:54px;height:54px;}
  .system-note{
    position:absolute;left:104px;top:1050px;margin:0;white-space:nowrap;
    font-family:"Bitter",serif;font-weight:700;font-size:29px;color:var(--white);line-height:1;
  }
  .benefits{
    position:absolute;left:104px;top:1102px;margin:0;padding:0;list-style:none;
    display:flex;gap:26px;white-space:nowrap;
    font-family:"Bitter",serif;font-weight:400;font-size:21px;color:var(--white);line-height:1;
  }
  .benefits li{display:flex;align-items:center;gap:8px;}
  .benefits svg{width:18px;height:18px;flex:none;}
</style>
</head>
<body>
<main class="canvas">
  <svg class="backdrop" viewBox="0 0 1200 1200">
    <defs>
      <linearGradient id="sandGrad" x1="0" y1="0" x2="1" y2="0">
        <stop offset="0" stop-color="#e9dfa6"/>
        <stop offset="1" stop-color="#eddb8a"/>
      </linearGradient>
      <linearGradient id="oliveGrad" x1="0" y1="0" x2="1" y2="1">
        <stop offset="0" stop-color="#a8974a"/>
        <stop offset="0.5" stop-color="#7d6d25"/>
        <stop offset="1" stop-color="#c4b673"/>
      </linearGradient>
      <linearGradient id="studentGrad" x1="0" y1="0" x2="1" y2="1">
        <stop offset="0" stop-color="#d9c3a8"/>
        <stop offset="1" stop-color="#b9c3d8"/>
      </linearGradient>
    </defs>
    <rect width="1200" height="1200" fill="url(#sandGrad)"/>
    <polygon class="classroom-photo" role="img" aria-label="Blurred classroom background photo"
      points="0,588 1200,120 1200,1200 0,1200" fill="url(#oliveGrad)"/>
    <polygon class="light-band" points="0,394 760,250 760,290 0,430" fill="var(--band)" opacity="0.85"/>
    <polygon class="student-photo" role="img" aria-label="Photo of a smiling young student at a computer"
      points="1010,0 1200,0 1200,1200 1169,1200 645,800 760,740 760,250"
      fill="url(#studentGrad)"/>
    <polygon class="light-band" points="0,468 1200,1180 1200,1200 1169,1200 0,505" fill="var(--band)" opacity="0.75"/>
    <polygon class="navy-field" points="0,535 1129,1200 0,1200" fill="var(--navy)"/>
  </svg>

  <div class="brand"><span class="brand-square"></span>Zorvale Academy</div>

  <h1 class="headline headline-top">Be part</h1>
  <p class="headline headline-mid">of something</p>
  <p class="headline headline-big">big</p>

  <a class="enroll-button" href="#">Click to Enroll Online Now</a>
  <svg class="cursor-icon" viewBox="0 0 50 50" aria-hidden="true">
    <g stroke="var(--spark)" stroke-width="2.5" stroke-linecap="round">
      <line x1="10" y1="3" x2="10" y2="9"/><line x1="1" y1="13" x2="7" y2="13"/>
      <line x1="4" y1="5" x2="7" y2="9"/><line x1="3" y1="22" x2="7" y2="18"/>
      <line x1="17" y1="4" x2="14" y2="8"/>
    </g>
    <path d="M14 14 L14 38 L20 32 L25 43 L30 41 L25 30 L33 30 Z" fill="#fff" stroke="var(--navy)" stroke-width="1.5"/>
  </svg>

  <p class="system-note">Online Learning Management system (ZOR-LMS)</p>
  <ul class="benefits">
    <li><svg viewBox="0 0 18 18" aria-hidden="true"><path d="M3 9.5 L7.5 14 L15 4.5" fill="none" stroke="var(--spark)" stroke-width="2.6" stroke-linecap="round" stroke-linejoin="round"/></svg>Learn anytime</li>
    <li><svg viewBox="0 0 18 18" aria-hidden="true"><path d="M3 9.5 L7.5 14 L15 4.5" fill="none" stroke="var(--spark)" stroke-width="2.6" stroke-linecap="round" stroke-linejoin="round"/></svg>Track progress</li>
    <li><svg viewBox="0 0 18 18" aria-hidden="true"><path d="M3 9.5 L7.5 14 L15 4.5" fill="none" stroke="var(--spark)" stroke-width="2.6" stroke-linecap="round" stroke-linejoin="round"/></svg>Teacher support</li>
  </ul>
</main>
</body>
</html>
```